A5 Flyer for Financial Services Business

I am after a re-design of our business flyer to fit in with our new branding style and logo colour scheme. Wanting something with a bit of designer flair that I could not create myself. I have included the flyer which I created which lacks style so dazzle me.

I want to use the same content.

Text for main body of flyer is

Are you a small business owner, tradie or PAVC Service Provider struggling to stay on top of your bookkeeping and compliance obligations? If so we would love to help you get back on track and take control of your business finances so that you can make informed business decisions and focus on what you do best.

We have over 20 years industry experience and, as a small business ourselves, we are able to offer our clients a personal bookkeeping solution tailored to meet the needs of your business.

Accounts Payable | Accounts Receivable
Customer Invoicing
Bank and Credit Card Reconciliations
Payroll | Superannuation | Payroll Tax
Business Activity | Instalment Activity Statements
Regular Financial Reports
Cloudbooks and Ledgerly Set-Up and Training

```html
<!DOCTYPE html>
<html lang="en">
<head>
<meta charset="utf-8">
<title>Even Ledger Financial Services – Bookkeeping Flyer</title>
<link href="https://fonts.googleapis.com/css2?family=Montserrat:wght@400;600;700;800&family=Open+Sans:wght@400;600&display=swap" rel="stylesheet">
<style>
  :root{
    --teal:#1fa3a4;
    --teal-dark:#0f7f82;
    --ink:#2c3338;
    --body:#4a5358;
    --paper:#ffffff;
    --paper-tint:#f1f3f4;
    --badge:#cfd6d9;
    --white:#ffffff;
  }
  *{box-sizing:border-box;margin:0;padding:0}
  html,body{width:847px;height:1200px;overflow:hidden;background:var(--paper)}
  .flyer{position:relative;width:847px;height:1200px;overflow:hidden;
    background:linear-gradient(180deg,var(--paper-tint) 0,var(--paper) 420px,var(--paper) 100%);
    font-family:'Open Sans',Arial,sans-serif;color:var(--body)}

  .photo{position:absolute}
  .photo-team{left:0;top:238px;width:372px;height:288px;
    background:linear-gradient(135deg,#e8e2da 0%,#cbbfb2 35%,#a9927f 65%,#6f6a70 100%);
    clip-path:polygon(0 0,100% 0,100% 100%,0 100%)}
  .photo-desk{left:0;top:526px;width:372px;height:404px;
    background:linear-gradient(160deg,#f4f6f7 0%,#dfe4e7 40%,#b7c0c6 75%,#8c969d 100%);
    clip-path:polygon(0 0,100% 0,100% 88%,0 100%)}
  .photo-crowd{left:318px;top:790px;width:529px;height:368px;
    background:linear-gradient(180deg,#e9edf0 0%,#cfd6db 30%,#b99c86 62%,#6d7f99 100%);
    clip-path:polygon(14% 0,100% 0,100% 100%,0 100%)}

  .headline-band{position:absolute;left:0;top:70px;width:372px;height:160px;background:var(--teal);
    clip-path:polygon(0 0,90% 0,100% 50%,90% 100%,0 100%);
    display:flex;align-items:center;padding-left:26px}
  .headline{font-family:'Montserrat',Arial,sans-serif;font-weight:800;color:var(--white);
    font-size:26px;line-height:1.45;letter-spacing:.2px;text-transform:uppercase}

  .brand{position:absolute;left:420px;top:26px;width:410px;text-align:center}
  .brand-mark{width:84px;height:84px;margin:0 auto 10px;background:var(--teal-dark);border-radius:50%}
  .brand-name{font-family:'Montserrat',Arial,sans-serif;font-weight:400;color:var(--teal-dark);
    font-size:36px;letter-spacing:2px;line-height:1.1;text-transform:uppercase}
  .brand-sub{font-family:'Montserrat',Arial,sans-serif;font-weight:400;color:var(--teal-dark);
    font-size:24px;letter-spacing:3px;margin-top:2px}

  .intro{position:absolute;left:432px;top:272px;width:392px;font-size:15px;line-height:1.5}
  .intro p+p{margin-top:18px}

  .services{position:absolute;left:432px;top:556px;width:372px;list-style:none;
    font-family:'Montserrat',Arial,sans-serif;font-weight:700;color:var(--teal);font-size:16px;line-height:1.55}

  .side-arrow{position:absolute;right:0;top:680px;width:34px;height:52px;background:var(--teal);
    clip-path:polygon(100% 0,0 50%,100% 100%)}

  .badges{position:absolute;left:20px;top:1010px;display:flex;gap:22px;align-items:center}
  .badge{width:100px;height:100px;background:var(--badge);border-radius:50%}
  .badge.square{border-radius:6px;background:#d8dcdd}

  .phone-box{position:absolute;left:460px;top:1036px;width:387px;height:86px;background:var(--teal);
    display:flex;align-items:center;justify-content:center;gap:14px;
    font-family:'Montserrat',Arial,sans-serif;font-weight:700;color:var(--white);font-size:44px;letter-spacing:1px}

  .website{position:absolute;left:22px;top:1160px;font-family:'Montserrat',Arial,sans-serif;
    font-weight:600;color:var(--teal-dark);font-size:15px}
</style>
</head>
<body>
<main class="flyer">
  <div class="headline-band">
    <h1 class="headline">Bookkeeping<br>tailored to your<br>business needs</h1>
  </div>

  <header class="brand">
    <div class="brand-mark"></div>
    <div class="brand-name">Even Ledger</div>
    <div class="brand-sub">Financial Services</div>
  </header>

  <div class="photo photo-team" role="img" aria-label="Photo of a smiling team of women working together at a laptop"></div>
  <div class="photo photo-desk" role="img" aria-label="Photo of hands using a calculator and writing on paperwork beside a laptop"></div>

  <section class="intro">
    <p>Are you a small business owner, tradie or PAVC Service Provider struggling to stay on top of your bookkeeping and compliance obligations? If so we would love to help you get back on track and take control of your business finances so that you can make informed business decisions and focus on what you do best.</p>
    <p>We have over 20 years industry experience and, as a small business ourselves, we are able to offer our clients a personal bookkeeping solution tailored to meet the needs of your business.</p>
  </section>

  <ul class="services">
    <li>Accounts Payable | Accounts Receivable</li>
    <li>Customer Invoicing</li>
    <li>Bank and Credit Card Reconciliations</li>
    <li>Payroll | Superannuation | Payroll Tax</li>
    <li>Business Activity | Instalment Activity Statements</li>
    <li>Regular Financial Reports</li>
    <li>Cloudbooks and Ledgerly Set-Up and Training</li>
  </ul>

  <div class="side-arrow"></div>

  <div class="photo photo-crowd" role="img" aria-label="Photo of a happy group of business people giving thumbs up"></div>

  <div class="badges">
    <div class="badge"></div>
    <div class="badge"></div>
    <div class="badge square"></div>
  </div>

  <div class="phone-box">
    <svg width="34" height="34" viewBox="0 0 24 24" aria-hidden="true"><path fill="#fff" d="M6.6 10.8a15.1 15.1 0 0 0 6.6 6.6l2.2-2.2a1 1 0 0 1 1-.25 11.4 11.4 0 0 0 3.6.57 1 1 0 0 1 1 1V20a1 1 0 0 1-1 1A17 17 0 0 1 3 4a1 1 0 0 1 1-1h3.5a1 1 0 0 1 1 1c0 1.25.2 2.45.57 3.57a1 1 0 0 1-.25 1z"/></svg>
    <span>0400 318 562</span>
  </div>

  <div class="website">www.evenledgerfinancial.com.au</div>
</main>
</body>
</html>
```